Kestrel Vitality a Centre Pty Ltd

Business card is to promote and represent our new business. It's situated in
47 Fenwick Road
Brookvale 2100 Sydney
Our clinic is all about getting people back to great health giving them back their lifestyle in half the usual time it takes to get results elsewhere , we do this through innovative therapies with latest state of the art equipment ,skills ,knowledge and experience.
We give them back their pain free healthy lifestyle with lots of energy to love life and perform their best Quickly and effectively .
The final design should communicate
Trust , confidence, results .
Updates

Reason: Waiting for some designers to submit work Thanks

Target Market(s)

High end clients that take their health and results seriously ,
High end athletes , as well as general people that want to see results with different
Treatment Methods and approach

Industry/Entity Type

Clinic

Contact Information for Business Card

Kestrel Vitality Centre Pty Ltd
47 Fenwick Road Brookvale 2100 Sydney
Website www.kestrelvitalitycentre.com.au

Font styles to use
Other font styles liked:
• Gothic font medium

Requirements
Must have
• A designe that makes people look twice with a wow factor , a designe that isn't like all the rest .
• Must have the logo in the colours Iv provided in my files
• Must communicate Trust, confidence , results
Nice to have
• 1) The logo raised up or
• 2) Maybe a pop up logo on the card ?
• Or let's be creative and have two cards one on top of the other so the two cards slide .... The front will have the kestrel logo with the address details etc
• The other card with have
• eg your next app .......................................repeating all way down the card
Should not have
• Basic plain looking card that everyone else has

```html
<!DOCTYPE html>
<html lang="en">
<head>
<meta charset="utf-8">
<title>Kestrel Vitality Centre – Business Cards</title>
<link rel="stylesheet" href="https://fonts.googleapis.com/css2?family=Didact+Gothic&family=Lora:wght@400&display=swap">
<style>
  :root{
    --backdrop:#e9e6e1;
    --card:#ffffff;
    --violet:#3d3f9a;
    --blue:#2aa3dc;
    --green:#8cc63f;
    --ink:#4a4a4a;
    --muted:#7a7a7a;
  }
  html,body{margin:0;padding:0;overflow:hidden;}
  body{width:1200px;height:1023px;background:var(--backdrop);position:relative;font-family:"Didact Gothic",sans-serif;}
  .card{position:absolute;width:540px;height:309px;background:var(--card);border-radius:4px;box-shadow:0 6px 18px rgba(0,0,0,.18);overflow:hidden;}
  .card-back{left:50px;top:190px;}
  .card-front{left:610px;top:524px;}
  .card svg.sweeps{position:absolute;left:0;top:0;width:540px;height:309px;}

  /* back card */
  .brand-block{position:absolute;left:250px;top:18px;}
  .brand-name{font-size:52px;line-height:1;color:var(--violet);letter-spacing:1px;}
  .brand-sub{font-size:12px;letter-spacing:8px;color:var(--green);margin-top:4px;}
  .brand-web{font-size:12px;color:var(--violet);letter-spacing:1px;margin-top:6px;}
  .appointment{position:absolute;left:318px;top:192px;width:196px;}
  .appointment-label{font-size:14px;color:#222;font-weight:bold;}
  .appointment-line{border-bottom:1.5px dotted #333;height:22px;}

  /* front card */
  .front-brand{position:absolute;left:40px;top:36px;display:flex;align-items:center;gap:14px;}
  .front-brand .dot{width:46px;height:46px;border-radius:50%;background:var(--green);}
  .front-brand .brand-name{font-size:48px;}
  .front-brand .brand-sub{font-size:11px;letter-spacing:7px;}
  .person{position:absolute;right:112px;top:122px;text-align:right;}
  .person-name{font-family:"Lora",serif;font-size:18px;color:var(--green);letter-spacing:1px;}
  .person-role{font-family:"Lora",serif;font-size:11px;color:var(--muted);}
  .contact{position:absolute;left:30px;top:196px;font-size:12px;color:var(--ink);line-height:17px;}
  .contact-row{display:flex;align-items:center;gap:6px;}
  .contact-icon{width:10px;height:10px;background:var(--green);border-radius:2px;flex:none;}
  .company{color:var(--green);}
</style>
</head>
<body>

<section class="card card-back" aria-label="Appointment card">
  <svg class="sweeps" viewBox="0 0 540 309" aria-hidden="true">
    <defs>
      <linearGradient id="sweepA" x1="0" y1="0" x2="0" y2="1">
        <stop offset="0" stop-color="#3d3f9a"/><stop offset=".5" stop-color="#2aa3dc"/><stop offset="1" stop-color="#8cc63f"/>
      </linearGradient>
      <linearGradient id="sweepB" x1="0" y1="1" x2="1" y2="0">
        <stop offset="0" stop-color="#3d3f9a"/><stop offset=".4" stop-color="#2aa3dc"/><stop offset="1" stop-color="#8cc63f"/>
      </linearGradient>
    </defs>
    <path d="M30 0 C180 50 230 170 190 309" fill="none" stroke="url(#sweepA)" stroke-width="4"/>
    <path d="M262 309 C240 200 320 125 540 120" fill="none" stroke="url(#sweepB)" stroke-width="4"/>
  </svg>
  <div class="brand-block">
    <div class="brand-name">Kestrel</div>
    <div class="brand-sub">VITALITY CENTRE</div>
    <div class="brand-web">www.kestrelvitalitycentre.com.au</div>
  </div>
  <div class="appointment">
    <div class="appointment-label">Next appointment:</div>
    <div class="appointment-line"></div>
    <div class="appointment-line"></div>
    <div class="appointment-line"></div>
    <div class="appointment-line"></div>
  </div>
</section>

<section class="card card-front" aria-label="Business card">
  <svg class="sweeps" viewBox="0 0 540 309" aria-hidden="true">
    <defs>
      <linearGradient id="sweepC" x1="0" y1="0" x2="1" y2="0">
        <stop offset="0" stop-color="#3d3f9a"/><stop offset="1" stop-color="#2aa3dc"/>
      </linearGradient>
      <linearGradient id="sweepD" x1="0" y1="0" x2="0" y2="1">
        <stop offset="0" stop-color="#2aa3dc"/><stop offset="1" stop-color="#8cc63f"/>
      </linearGradient>
    </defs>
    <path d="M0 150 C100 125 190 150 255 178" fill="none" stroke="url(#sweepC)" stroke-width="4"/>
    <path d="M445 115 C520 150 535 250 500 309" fill="none" stroke="url(#sweepD)" stroke-width="4"/>
  </svg>
  <div class="front-brand">
    <div class="dot"></div>
    <div>
      <div class="brand-name">Kestrel</div>
      <div class="brand-sub">VITALITY CENTRE</div>
    </div>
  </div>
  <div class="person">
    <div class="person-name">LIAM HARCOURT</div>
    <div class="person-role">Director</div>
  </div>
  <div class="contact">
    <div class="contact-row"><span class="contact-icon"></span>0412 555 018</div>
    <div class="contact-row"><span class="contact-icon"></span>0298 555 043</div>
    <div class="contact-row"><span class="contact-icon"></span>liamharcourt@kestrelvitalitycentre.com.au</div>
    <div class="company">Kestrel Vitality Centre Pty Ltd</div>
    <div>47 Fenwick Road, Brookvale 2100 Sydney</div>
  </div>
</section>

</body>
</html>
```